Coaching and Tutoring that removes all obstacles and leads to success and happiness

Tutoring maths giving confidence, clarity and success to students of all abilities. Tutoring from 14 years to 18 years old. Dealing with exam preparation and stress.
Coaching confidence, resilience and ultimately happiness and freedom.
The design to inspire and reassure people of a safe pair of hands as well excitement of the beginning of something new in their lives.

Target Market(s)

20 -30 year olds

Industry/Entity Type

Self Development and Education

Contact Information for Business Card

Confidence Coach and Maths Tutor

Font styles to use
Sans Serif

Colors
EE7325
F08F49
F5BC92
FAE3D3
FDF4ED

Requirements
Must have
• Success and Happiness

```html
<!DOCTYPE html>
<html lang="en">
<head>
<meta charset="utf-8">
<title>Bright &amp; Steady — Business Card</title>
<link rel="stylesheet" href="https://fonts.googleapis.com/css2?family=Montserrat:wght@800&family=Roboto:wght@400;500&display=swap">
<style>
  :root {
    --backdrop: #2a2a2a;
    --orange: #ee7325;
    --orange-mid: #f08f49;
    --peach: #f5bc92;
    --blush: #fae3d3;
    --cream: #fdf4ed;
    --ink: #3a2a20;
    --charcoal: #3a3e41;
    --white: #ffffff;
  }
  html, body {
    margin: 0;
    width: 1200px;
    height: 1138px;
    overflow: hidden;
    background: var(--backdrop);
  }
  .card {
    position: absolute;
    border-radius: 15px;
    overflow: hidden;
  }
  .card-front {
    left: 274px; top: 186px; width: 623px; height: 376px;
    background: linear-gradient(135deg, var(--orange-mid) 0%, var(--orange) 100%);
    color: var(--white);
    text-align: center;
  }
  .brand-name {
    font-family: "Montserrat", sans-serif;
    font-weight: 800;
    margin: 0;
    letter-spacing: -0.01em;
    line-height: 1;
  }
  .brand-tagline {
    font-family: "Montserrat", sans-serif;
    font-weight: 800;
    margin: 0;
    text-transform: uppercase;
    line-height: 1;
  }
  .card-front .brand-name {
    position: absolute; left: 0; right: 0; top: 136px;
    font-size: 53px;
  }
  .card-front .brand-tagline {
    position: absolute; left: 0; right: 0; top: 199px;
    font-size: 15px; letter-spacing: 0.95em; padding-left: 0.95em;
  }
  .card-front .motto {
    position: absolute; left: 0; right: 0; top: 236px; margin: 0;
    font-family: "Roboto", sans-serif; font-weight: 500;
    font-size: 16px; color: var(--cream); letter-spacing: 0.06em;
  }
  .card-front .site {
    position: absolute; left: 0; right: 0; top: 331px;
    font-family: "Roboto", sans-serif; font-size: 14px;
    letter-spacing: 0.32em; margin: 0;
  }
  .card-back {
    left: 276px; top: 608px; width: 618px; height: 374px;
    background: linear-gradient(180deg, var(--cream) 0%, var(--blush) 100%);
    color: var(--ink);
  }
  .card-back .brand-name {
    position: absolute; left: 30px; top: 64px;
    font-size: 33px; color: var(--orange);
  }
  .card-back .brand-tagline {
    position: absolute; left: 32px; top: 100px;
    font-size: 10.5px; letter-spacing: 1.02em; color: var(--ink);
  }
  .edge-dot {
    position: absolute; left: -48px; top: 196px;
    width: 60px; height: 60px; border-radius: 50%;
    background: var(--orange);
  }
  .person-name {
    position: absolute; left: 30px; top: 201px; margin: 0;
    font-family: "Roboto", sans-serif; font-weight: 500;
    font-size: 22px; color: var(--orange);
  }
  .person-role {
    position: absolute; left: 30px; top: 230px; margin: 0;
    font-family: "Roboto", sans-serif; font-size: 15px; color: var(--ink);
  }
  .contacts {
    position: absolute; left: 30px; top: 276px;
    list-style: none; margin: 0; padding: 0;
    font-family: "Roboto", sans-serif; font-size: 16px; color: var(--ink);
  }
  .contacts li {
    display: flex; align-items: center; height: 23.5px;
  }
  .contacts svg { width: 14px; height: 14px; margin-right: 18px; color: var(--orange); fill: currentColor; }
  .brand-mark {
    position: absolute; left: 330px; top: 60px; width: 280px; height: 290px;
    text-align: center;
  }
  .brand-mark .dot {
    width: 150px; height: 150px; border-radius: 50%;
    background: var(--peach); margin: 20px auto 26px;
  }
  .brand-mark .mark-name {
    font-family: "Montserrat", sans-serif; font-weight: 800;
    font-size: 26px; color: var(--orange); margin: 0;
  }
</style>
</head>
<body>
  <section class="card card-front" aria-label="Card front">
    <h1 class="brand-name">Bright &amp; Steady</h1>
    <p class="brand-tagline">Coach and Tutor</p>
    <p class="motto">Success and Happiness</p>
    <p class="site">www.brightsteady.net</p>
  </section>

  <section class="card card-back" aria-label="Card back">
    <h2 class="brand-name">Bright &amp; Steady</h2>
    <p class="brand-tagline">Coach and Tutor</p>
    <div class="edge-dot"></div>
    <p class="person-name">Alex Rowan Hale</p>
    <p class="person-role">Managing Director</p>
    <ul class="contacts">
      <li>
        <svg viewBox="0 0 16 16" aria-hidden="true"><path d="M1 5c0-2 3-3 7-3s7 1 7 3v1h-4V4.8C9.8 4.5 6.2 4.5 5 4.8V6H1z"/><path d="M4 7h8l2 7H2z"/></svg>
        555-014-2026
      </li>
      <li>
        <svg viewBox="0 0 16 16" aria-hidden="true"><path d="M1 3h14v10H1z M2.5 4.5 8 9l5.5-4.5" fill="none" stroke="currentColor" stroke-width="1.8"/></svg>
        alex@brightsteady.net
      </li>
      <li>
        <svg viewBox="0 0 16 16" aria-hidden="true"><g fill="none" stroke="currentColor" stroke-width="1.4"><circle cx="8" cy="8" r="6.5"/><ellipse cx="8" cy="8" rx="3" ry="6.5"/><path d="M1.5 8h13M2.5 4.8h11M2.5 11.2h11"/></g></svg>
        www.brightsteady.net
      </li>
    </ul>
    <div class="brand-mark">
      <div class="dot"></div>
      <p class="mark-name">Bright &amp; Steady</p>
    </div>
  </section>
</body>
</html>
```